High-end law practice specializing in closely held business succession planning and complex estates

Solo practitioner whose practice specializes in high-net worth, complex estate planning needs muliple versions of letterhead black and white, please. Letterhead should incorporate slogan, "Protecting your family business is my business," for one and "Complex Estate Planning"; third with no slogan. All for The Law Office of Merel Kate Dunholt, PC, 418 Calder Pond Ln., Newport News, Virginia 23601, Tel. 757-641-3925 Fax tbd email: merel@mkdcounsel.example; Merel Kate Dunholt, Esq., principal, licensed in VA, NY, DC

Reason: My internet service went down and I can only view designs on my smart phone -- it's just too hard to review. So sorry! Working with my ISP now. Please be patient!

Target Market(s)

High net worth clients with complex estate planning needs, family businesses, family farmers, family foresters -- people with unique estate/succession planning needs who need a specialist who understands them.

Industry/Entity Type

Business

Font styles to use
Script

Requirements
Must have
• A high-end look and feel, connoting trustworthiness, special knowledge, and expertise.

```html
<!DOCTYPE html>
<html lang="en">
<head>
<meta charset="utf-8">
<title>Letterhead – The Law Office of Merel Kate Dunholt, PC</title>
<link rel="stylesheet" href="https://fonts.googleapis.com/css2?family=Crimson+Pro:wght@400;600&display=swap">
<style>
  :root {
    --backdrop: #cfcfcf;
    --paper: #f0f0f0;
    --ink: #1e1e1e;
    --rule: #6a6a6a;
    --band: #232323;
  }
  * { margin: 0; padding: 0; box-sizing: border-box; }
  html, body {
    width: 1200px;
    height: 1041px;
    overflow: hidden;
    background: var(--backdrop);
  }
  body { position: relative; font-family: "Crimson Pro", Georgia, serif; color: var(--ink); }

  .letterhead {
    position: absolute;
    left: 280px;
    top: 106px;
    width: 640px;
    height: 826px;
    background: var(--paper);
  }

  .firm-name { position: absolute; left: 40px; top: 0; font-weight: 400; color: var(--ink); }
  .firm-initials {
    position: absolute;
    left: 0;
    top: 52px;
    font-size: 37px;
    line-height: 37px;
    letter-spacing: 0.5px;
    white-space: nowrap;
  }
  .firm-title {
    position: absolute;
    left: 91px;
    top: 50px;
    font-size: 23px;
    line-height: 24px;
    white-space: nowrap;
  }
  .firm-subtitle {
    position: absolute;
    left: 95px;
    top: 76px;
    font-size: 10.5px;
    line-height: 12px;
    letter-spacing: 0.3px;
    text-transform: uppercase;
    white-space: nowrap;
  }

  .contact-block {
    position: absolute;
    top: 56px;
    font-size: 8px;
    line-height: 10.3px;
    white-space: nowrap;
  }
  .contact-block strong { font-weight: 600; }
  .contact-attorney { left: 330px; }
  .contact-lines { left: 434px; }
  .contact-address { left: 545px; }

  .contact-rule {
    position: absolute;
    top: 58px;
    width: 1px;
    height: 26px;
    background: var(--rule);
  }
  .rule-one { left: 424px; }
  .rule-two { left: 536px; }

  .footer-band {
    position: absolute;
    left: 0;
    bottom: 0;
    width: 100%;
    height: 8px;
    background: var(--band);
  }
</style>
</head>
<body>
  <main class="letterhead">
    <header>
      <div class="firm-name">
        <span class="firm-initials">MKD</span>
        <span class="firm-title">The Law Office</span>
        <span class="firm-subtitle">of Merel Kate Dunholt, PC</span>
      </div>

      <address class="contact-block contact-attorney">
        <strong>Merel Kate Dunholt</strong>, Esq.<br>
        Principal<br>
        Licensed in VA, NY, DC
      </address>
      <span class="contact-rule rule-one"></span>
      <address class="contact-block contact-lines">
        T: 757-641-3925<br>
        F: 757-641-3927<br>
        E: merel@mkdcounsel.example
      </address>
      <span class="contact-rule rule-two"></span>
      <address class="contact-block contact-address">
        418 Calder Pond Ln.<br>
        Newport News<br>
        Virginia 23601
      </address>
    </header>
    <div class="footer-band"></div>
  </main>
</body>
</html>
```